Executive Coaching Consultancy Website Design

I am setting up an executive coaching consultancy practice, primarily targeting ambitious women (and men of course!) who want to progress to the next level in their careers (late 20's to mid forties in age) or who are returning to work after a career break. I need a simple website that promotes the benefits of my consultancy service, contact details plus other associated information and incorporates social media channels so I can update information and news items on a regular basis. It would be useful to have a design for a Brixwell dedicated page too.

This project has been on the back burner for a while due to other commitments, however when I originally decided to set the business up a couple of years ago, I did get a logo and some illustrations for the website designed and produced - which I've uploaded.

The design should convey expertise, understanding, serenity and trust. I am keen it appears stylish and different to many of the other coaching websites that use typical business imagery and are very cluttered. I am targeting individuals who want to invest their own time and money into getting to the next step (as opposed to targeting HR teams in large organisations).

The design should also be responsive so the target audience can easily view it on their phones/tablets.

Initially the information to be conveyed on the website will include:

- How coaching can improve career performance
- The coaching process and what to expect
- Fees
- About us
- Contact details
- A Blog
- Links to useful articles/organisations

etc.

A simple scroll down format would make sense but I will leave it to your best judgement!

Many thanks!!
Updates

Project Deadline Extended
Reason: Realised it was still the holiday period but am keen to receive prospective designs so I can commission this project quickly. Thanks!

Target Market(s)

28-45 yr old career women

Industry/Entity Type

Business

Number of Pages Required

2 page

Requirements
Must have
• Clean, simple intuitive navigation that can be adapted easily for responsive design purposes
Nice to have
• Area for testimonials
Should not have
• Cluttered information.

```html
<!DOCTYPE html>
<html lang="en">
<head>
<meta charset="utf-8">
<title>Harrow Lane Coaching</title>
<link href="https://fonts.googleapis.com/css2?family=Open+Sans:wght@400;600;700;800&display=swap" rel="stylesheet">
<style>
:root{
  --teal:#5cbdb9;
  --teal-dark:#3f9f9b;
  --red:#e3363b;
  --ink:#333333;
  --muted:#6a6a6a;
  --dark:#2e2e2e;
  --darker:#242424;
  --grey:#ececec;
  --line:#d5d5d5;
  --white:#ffffff;
}
*{box-sizing:border-box;margin:0;padding:0}
html,body{width:1200px;height:3356px;overflow:hidden}
body{font-family:"Open Sans",Arial,sans-serif;color:var(--ink);background:var(--white);font-size:14px;line-height:1.6}
.wrap{width:960px;margin:0 auto;position:relative;height:100%}
section,header,nav,footer{position:relative;width:1200px;overflow:hidden}

/* header */
.site-header{height:120px}
.brand{position:absolute;left:0;top:30px;display:flex;align-items:center;gap:14px}
.brand-dot{width:44px;height:44px;border-radius:50%;background:var(--red)}
.brand-name{font-weight:700;font-size:20px;letter-spacing:2px;color:var(--ink);text-transform:uppercase;line-height:1.2}
.header-contact{position:absolute;right:0;top:22px;text-align:right;font-size:13px;color:var(--muted)}
.header-contact .phone{display:flex;align-items:center;justify-content:flex-end;gap:8px;font-weight:600;color:var(--ink)}
.follow{margin-top:6px;display:flex;gap:8px;justify-content:flex-end;align-items:center}
.follow span.lbl{color:var(--red);font-weight:700}
.follow span.net{font-size:11px;color:var(--muted)}

/* nav */
.main-nav{height:40px;background:var(--teal)}
.main-nav ul{list-style:none;display:flex;height:40px;align-items:center}
.main-nav li{color:var(--white);font-size:13px;font-weight:600;padding:0 18px;height:40px;line-height:40px}
.main-nav li.active{background:var(--teal-dark)}
.main-nav .demo{position:absolute;right:0;top:6px;height:28px;line-height:28px;padding:0 16px;background:var(--dark);color:var(--white);font-size:12px;font-weight:700;text-transform:uppercase}

/* hero */
.hero{height:380px;background:linear-gradient(90deg,#2b2b2b 0%,#3a3a3a 45%,#5a5a5a 100%)}
.hero-photo{position:absolute;right:0;top:0;width:560px;height:380px;background:linear-gradient(100deg,#3a3a3a 0%,#8b8f94 55%,#c9ccd0 100%)}
.hero-copy{position:absolute;left:0;top:36px;width:560px;color:var(--white)}
.hero-copy h1{font-size:24px;font-weight:700;color:var(--red);margin-bottom:14px;white-space:nowrap}
.hero-copy ul{list-style:none}
.hero-copy li{font-size:14px;font-weight:600;padding-left:18px;position:relative;line-height:1.7}
.hero-copy li::before{content:"";position:absolute;left:0;top:9px;width:7px;height:7px;background:var(--white);border-radius:50%}
.btn{display:inline-block;font-weight:700;font-size:13px;color:var(--white);padding:10px 22px}
.hero .btn{background:var(--dark);margin-top:22px;border:1px solid #555}

/* section titles */
.section-title{font-size:26px;font-weight:600;text-transform:uppercase;text-align:center;color:var(--ink);letter-spacing:.5px}
.section-title::after{content:"";display:block;width:60px;height:2px;background:var(--teal);margin:10px auto 0}
.lead{text-align:center;color:var(--muted);font-size:14px}

/* welcome */
.welcome{height:392px}
.welcome .section-title{padding-top:36px}
.welcome .lead{width:780px;margin:18px auto 0}
.features{display:flex;gap:30px;margin-top:58px;justify-content:center}
.feature{width:300px;height:118px;border:1px solid var(--line);position:relative;text-align:center;padding:42px 18px 0}
.feature .icon{position:absolute;left:50%;top:-28px;margin-left:-28px;width:56px;height:56px;border-radius:50%;background:var(--white);border:2px solid var(--teal);display:flex;align-items:center;justify-content:center}
.feature h3{font-size:14px;font-weight:700;text-transform:uppercase}
.feature p{font-size:12px;color:var(--muted);line-height:1.5;margin-top:4px}

/* how */
.how{height:408px;background:var(--grey)}
.how .section-title{padding-top:30px}
.how-text{position:absolute;left:0;top:110px;width:430px;font-size:13px;color:var(--muted)}
.how-text ul{margin-top:12px;padding-left:18px}
.how-text li{line-height:1.7}
.how-figure{position:absolute;right:0;top:100px;width:480px;height:270px;background:linear-gradient(180deg,#ffffff,#f2f2f2);border:1px solid #dedede}

/* process */
.process{height:200px}
.process .section-title{padding-top:24px}
.process .lead{margin-top:18px;font-size:13px;text-align:justify;color:var(--muted)}

/* blog */
.blog{height:580px;background:var(--grey)}
.blog .section-title{padding-top:28px}
.posts{display:flex;gap:40px;margin-top:30px}
.post{width:460px}
.post-image{height:250px;background:linear-gradient(135deg,#3d4f63,#8fa3b3 60%,#c4ced6)}
.post-image.alt{background:linear-gradient(135deg,#e7e7e7,#b9bcbf 55%,#6f7378)}
.post h3{font-size:14px;font-weight:700;text-transform:uppercase;margin-top:16px}
.post p{font-size:12px;color:var(--muted);margin-top:6px;line-height:1.55}
.post-meta{display:flex;justify-content:space-between;align-items:center;margin-top:12px}
.post-meta .date{font-size:13px;font-weight:700}
.post-meta .btn{background:var(--dark);font-size:12px;padding:7px 14px}

/* links */
.links{height:280px}
.links .section-title{padding-top:24px}
.link-cols{display:flex;gap:40px;margin-top:24px}
.link-cols ul{list-style:none;width:250px}
.link-cols li{font-size:12px;color:var(--muted);padding-left:14px;position:relative;line-height:1.75}
.link-cols li::before{content:"";position:absolute;left:0;top:8px;width:5px;height:5px;border-right:1.5px solid var(--teal);border-bottom:1.5px solid var(--teal);transform:rotate(-45deg)}
.links-figure{width:300px;height:160px;background:radial-gradient(circle at 50% 50%,#d8eceb 0%,#f4f9f9 70%)}

/* fees */
.fees{height:240px;background:var(--grey)}
.fees .section-title{padding-top:26px}
.fees .lead{margin-top:16px;color:var(--ink);line-height:30px}
.fees .lead strong{font-size:20px}
.fee-buttons{display:flex;justify-content:center;gap:20px;margin-top:20px;position:relative}
.fee-buttons .btn{width:280px;text-align:center;font-size:16px;font-weight:600;padding:14px 0}
.btn-red{background:var(--red)}
.btn-teal{background:var(--teal)}
.offer{position:absolute;left:738px;top:-22px;width:60px;height:60px;border-radius:50%;background:var(--red);color:var(--white);font-size:10px;font-weight:800;text-transform:uppercase;display:flex;align-items:center;justify-content:center;text-align:center;line-height:1.2;transform:rotate(-12deg)}

/* touch */
.touch{height:80px}
.touch .section-title{padding-top:20px}

/* contact */
.contact{height:440px;background:var(--dark)}
.contact-form{position:absolute;left:0;top:36px;width:320px}
.field{display:flex;align-items:center;margin-bottom:14px}
.field label{width:70px;color:#cfcfcf;font-size:13px}
.field .input{flex:1;height:32px;background:var(--white)}
.field.detail{align-items:flex-start}
.field.detail .input{height:120px}
.contact-form .send{margin-left:70px;background:var(--white);color:var(--ink);font-size:12px;padding:6px 26px}
.map{position:absolute;right:0;top:36px;width:600px;height:370px;background:linear-gradient(135deg,#e9e5dc,#d6dcd0 50%,#e3e0d8)}

/* footer */
.site-footer{height:196px;background:var(--darker)}
.social{display:flex;justify-content:center;gap:12px;padding-top:76px}
.social li{list-style:none;height:44px;padding:0 14px;line-height:44px;background:#3a3a3a;color:var(--white);font-size:12px;font-weight:600}
</style>
</head>
<body>

<header class="site-header">
  <div class="wrap">
    <div class="brand">
      <span class="brand-dot"></span>
      <span class="brand-name">Harrow Lane<br>Coaching</span>
    </div>
    <div class="header-contact">
      <div class="phone">
        <svg width="14" height="14" viewBox="0 0 24 24"><path d="M6.6 10.8a15 15 0 0 0 6.6 6.6l2.2-2.2c.3-.3.7-.4 1-.2 1.1.4 2.3.6 3.6.6.6 0 1 .4 1 1V20c0 .6-.4 1-1 1C10.6 21 3 13.4 3 4c0-.6.4-1 1-1h3.5c.6 0 1 .4 1 1 0 1.3.2 2.5.6 3.6.1.3 0 .7-.2 1z" fill="#e3363b"/></svg>
        1-800-555-0142
      </div>
      <div class="follow"><span class="lbl">Follow Us</span><span class="net">Friendly</span><span class="net">Chirper</span><span class="net">Brixwell</span></div>
    </div>
  </div>
</header>

<nav class="main-nav">
  <div class="wrap">
    <ul>
      <li class="active">Home</li>
      <li>About Us</li>
      <li>What We Do?</li>
      <li>Coaching Process</li>
      <li>Fees</li>
      <li>Useful Links</li>
      <li>Blog</li>
      <li>Contact Us</li>
    </ul>
    <span class="demo">Request Demo</span>
  </div>
</nav>

<section class="hero">
  <div class="hero-photo" role="img" aria-label="Photo of a smiling executive in a suit giving a thumbs up"></div>
  <div class="wrap">
    <div class="hero-copy">
      <h1>Benefits of Executive Coaching Include:</h1>
      <ul>
        <li>Fast-track Leadership Development,</li>
        <li>Enhanced Leadership &amp; Strategic Planning Skills</li>
        <li>Better Decision-Making,</li>
        <li>Improved Goal Setting &amp; Faster Achievement of Goals,</li>
        <li>Ability To Inspire &amp; Motivate Teams, Including Across Geographically Dispersed Locations</li>
        <li>Confident Communication,</li>
        <li>Improved Working Relationships.</li>
      </ul>
      <span class="btn">Learn More</span>
    </div>
  </div>
</section>

<section class="welcome">
  <div class="wrap">
    <h2 class="section-title">Welcome to Harrow Lane Coaching</h2>
    <p class="lead">Executive coaching is one-to-one coaching. It is where a person works individually with an executive coach on their particular areas of strength and weakness in order to fulfil their potential. It is a catalyst for enhanced performance of the individual and the team they lead.</p>
    <div class="features">
      <div class="feature">
        <span class="icon"><svg width="28" height="28" viewBox="0 0 24 24"><path d="M3 20h18M5 16l5-5 4 3 6-7" fill="none" stroke="#5cbdb9" stroke-width="2"/></svg></span>
        <h3>Improve Career Performance</h3>
        <p>Build stronger skills, clearer goals and lasting confidence for your next career step.</p>
      </div>
      <div class="feature">
        <span class="icon"><svg width="28" height="28" viewBox="0 0 24 24"><circle cx="12" cy="12" r="4" fill="none" stroke="#5cbdb9" stroke-width="2"/><path d="M12 2v4M12 18v4M2 12h4M18 12h4M5 5l3 3M16 16l3 3M5 19l3-3M16 8l3-3" stroke="#5cbdb9" stroke-width="2"/></svg></span>
        <h3>Coaching Process</h3>
        <p>A clear, structured path from first meeting to measurable progress and review.</p>
      </div>
      <div class="feature">
        <span class="icon"><svg width="28" height="28" viewBox="0 0 24 24"><path d="M4 12l5 5L20 6" fill="none" stroke="#5cbdb9" stroke-width="2.4"/></svg></span>
        <h3>What to Expect</h3>
        <p>Confidential sessions, honest feedback and practical support at every stage.</p>
      </div>
    </div>
  </div>
</section>

<section class="how">
  <div class="wrap">
    <h2 class="section-title">How Coaching Can Improve Career Performance</h2>
    <div class="how-text">
      <p>Executive coaching is tailored to the needs of the individual. Some of the reasons for using executive coaching are:</p>
      <ul>
        <li>Preparation for role/career changes</li>
        <li>Managing stress, change, conflict or crisis</li>
        <li>Enhancing personal impact and performance</li>
        <li>Supporting the appointment of a person into a different role</li>
        <li>Accelerating the personal development of those with high potential</li>
        <li>Acting as an objective and independent sounding board to a senior individual</li>
        <li>Offering tailored development as a means of rewarding and retaining key staff critical to the business</li>
      </ul>
    </div>
    <div class="how-figure" role="img" aria-label="Illustration of a hand writing the word coaching surrounded by linked coaching keywords"></div>
  </div>
</section>

<section class="process">
  <div class="wrap">
    <h2 class="section-title">The Coaching Process</h2>
    <p class="lead">We deliver executive coaching sessions either face to face, by telephone or by video call, depending on what suits you best. Each programme begins with an initial conversation to agree your goals, the areas you want to focus on and how progress will be measured. Sessions are spaced to give you time to apply new approaches at work, reflect on results and bring fresh questions to the next meeting. Throughout the programme your coach offers honest feedback, practical tools and steady encouragement, and at the end we review progress together and agree the next steps for your continued development.</p>
  </div>
</section>

<section class="blog">
  <div class="wrap">
    <h2 class="section-title">News Form Blog</h2>
    <div class="posts">
      <article class="post">
        <div class="post-image" role="img" aria-label="Photo of financial charts and figures on a screen"></div>
        <h3>Evaluation and Return on Investment (ROI)</h3>
        <p>Measuring the value of coaching helps individuals and sponsors see real progress. We look at simple ways to track goals, gather feedback and understand the return on time and money invested in your development.</p>
        <div class="post-meta"><span class="date">21 Tuesday, 2014</span><span class="btn">Read More</span></div>
      </article>
      <article class="post">
        <div class="post-image alt" role="img" aria-label="Photo of a businessman in a suit giving a thumbs up"></div>
        <h3>Coach Training Programmes</h3>
        <p>After experiencing the benefits of coaching, many clients wish to learn the skills themselves. Our training programmes introduce the core methods so you can support colleagues and teams with confidence.</p>
        <div class="post-meta"><span class="date">21 Tuesday, 2014</span><span class="btn">Read More</span></div>
      </article>
    </div>
  </div>
</section>

<section class="links">
  <div class="wrap">
    <h2 class="section-title">Usefull Links</h2>
    <div class="link-cols">
      <ul>
        <li>Expert Training for Managers</li>
        <li>Leadership Development</li>
        <li>Expert Training - Certification</li>
        <li>Inner Game Of Leadership</li>
        <li>Sustainability Services (CSR)</li>
        <li>Franchise Trainer</li>
        <li>Coaching Evaluation</li>
      </ul>
      <ul>
        <li>Coach Training - Certification</li>
        <li>Coach Training for Managers</li>
        <li>Distance Coach Training</li>
        <li>Executive Coaching U.K</li>
        <li>Transpersonal Coach Training</li>
        <li>Inner Game of Leadership</li>
        <li>Transformation Skills for Leaders and Coaches</li>
      </ul>
      <div class="links-figure" role="img" aria-label="Illustration of a network of connected people"></div>
    </div>
  </div>
</section>

<section class="fees">
  <div class="wrap">
    <h2 class="section-title">Coaching Fees</h2>
    <p class="lead">For More Information or To Enroll by Phone <strong>Call Now : 1-800-555-0142</strong></p>
    <div class="fee-buttons">
      <span class="btn btn-red">Registration Information</span>
      <span class="btn btn-teal">Enroll Online Now</span>
      <span class="offer">Special<br>Offer</span>
    </div>
  </div>
</section>

<section class="touch">
  <div class="wrap">
    <h2 class="section-title">Get in Touch</h2>
  </div>
</section>

<section class="contact">
  <div class="wrap">
    <div class="contact-form">
      <div class="field"><label>Name *</label><span class="input"></span></div>
      <div class="field"><label>Email *</label><span class="input"></span></div>
      <div class="field"><label>Phone *</label><span class="input"></span></div>
      <div class="field detail"><label>Detail *</label><span class="input"></span></div>
      <span class="btn send">SEND</span>
    </div>
    <div class="map" role="img" aria-label="Street map showing the office location"></div>
  </div>
</section>

<footer class="site-footer">
  <ul class="social">
    <li>Friendly</li>
    <li>Chirper</li>
    <li>Brixwell</li>
    <li>Streamly</li>
    <li>Circles</li>
    <li>Feed</li>
  </ul>
</footer>

</body>
</html>
```